Fairhollow Terrace
WHERE EVERY DAY FEELS LIKE HOME
Professional
Delphine Marquist
Administrator
812 Quillon Avenue
Linwell,SD 57390
delphine.marquist@fairhollowterrace.org
www.fairhollowterrace.org
Here is the AI file.

```html
<!DOCTYPE html>
<html lang="en">
<head>
<meta charset="utf-8">
<title>Fairhollow Terrace – Business Card</title>
<link rel="stylesheet" href="https://fonts.googleapis.com/css2?family=Tinos:wght@400;700&display=swap">
<style>
  :root {
    --card-white: #ffffff;
    --brown-deep: #4a2e18;
    --brown-mid: #6e4a2c;
    --brown-light: #8c6745;
    --brown-text: #5a3a20;
    --tagline: #5e4a3a;
    --ink-light: #ffffff;
  }
  * { margin: 0; padding: 0; box-sizing: border-box; }
  html, body {
    width: 1200px;
    height: 686px;
    overflow: hidden;
    background: var(--card-white);
  }
  .card {
    position: relative;
    width: 1200px;
    height: 686px;
    background: var(--card-white);
    font-family: "Tinos", "Times New Roman", serif;
    overflow: hidden;
  }
  .card__backdrop {
    position: absolute;
    inset: 0;
    width: 1200px;
    height: 686px;
  }
  .brand {
    position: absolute;
    left: 48px;
    top: 268px;
    width: 470px;
    text-align: center;
  }
  .brand__name {
    font-size: 50px;
    font-weight: 400;
    color: var(--brown-text);
    letter-spacing: 1px;
    line-height: 1.1;
  }
  .brand__rule {
    height: 2px;
    background: var(--brown-text);
    margin: 12px 10px 10px;
  }
  .brand__tagline {
    font-size: 15px;
    letter-spacing: 4px;
    color: var(--tagline);
    white-space: nowrap;
  }
  .person {
    position: absolute;
    right: 32px;
    top: 30px;
    text-align: right;
    color: var(--ink-light);
  }
  .person__name {
    font-size: 37px;
    font-weight: 700;
    line-height: 1.2;
  }
  .person__role {
    font-size: 34px;
    font-weight: 400;
    line-height: 1.15;
  }
  .contact {
    position: absolute;
    right: 42px;
    bottom: 2px;
    text-align: right;
    color: var(--ink-light);
    font-size: 27px;
    line-height: 43px;
    list-style: none;
    white-space: nowrap;
  }
</style>
</head>
<body>
  <main class="card">
    <svg class="card__backdrop" viewBox="0 0 1200 686" aria-hidden="true">
      <defs>
        <linearGradient id="sweep-dark" x1="0" y1="0" x2="1" y2="1">
          <stop offset="0" stop-color="#6e4a2c"/>
          <stop offset="1" stop-color="#4a2e18"/>
        </linearGradient>
        <linearGradient id="sweep-light" x1="0" y1="0" x2="1" y2="1">
          <stop offset="0" stop-color="#8c6745"/>
          <stop offset="1" stop-color="#6e4a2c"/>
        </linearGradient>
      </defs>
      <path class="sweep sweep--outer" fill="url(#sweep-dark)"
            d="M750 0 C860 100 860 260 740 400 C620 540 390 650 150 686 L1200 686 L1200 0 Z"/>
      <path class="sweep sweep--inner" fill="url(#sweep-light)" opacity="0.55"
            d="M820 40 C910 150 890 300 770 430 C650 560 480 640 330 686 L700 686 C860 560 980 420 980 260 C980 150 910 80 820 40 Z"/>
    </svg>

    <header class="brand">
      <div class="brand__name">Fairhollow Terrace</div>
      <div class="brand__rule"></div>
      <div class="brand__tagline">WHERE EVERY DAY FEELS LIKE HOME</div>
    </header>

    <section class="person">
      <h1 class="person__name">Delphine Marquist</h1>
      <p class="person__role">Administrator</p>
    </section>

    <ul class="contact">
      <li class="contact__address">812 Quillon Avenue Linwell,SD 57390</li>
      <li class="contact__phone">Phone : (605) 555-0148</li>
      <li class="contact__email">Email : delphine.marquist@fairhollowterrace.org</li>
      <li class="contact__web">Web : www.fairhollowterrace.org</li>
    </ul>
  </main>
</body>
</html>
```